Business Card Design Project

We need a buisness card for a new digital sinage company. Our target cliants are small to mediaum buisness who want to advertise on out digital sinage network

Target Market(s)

Small to medium buisness

Industry/Entity Type

Digital

Requirements
Must have
• Must have logo

```html
<!DOCTYPE html>
<html lang="en">
<head>
<meta charset="utf-8">
<title>Glowcast – Business Card</title>
<link rel="stylesheet" href="https://fonts.googleapis.com/css2?family=Montserrat:ital,wght@0,400;0,500;0,700;0,800;1,400&display=swap">
<style>
  :root {
    --page-bg: #ecebe8;
    --card-front: #f4f6f8;
    --card-front-edge: #e3e8ec;
    --ink: #111418;
    --ink-soft: #2a2f35;
    --divider: #1c1f23;
    --map-tone-a: #dfe8ef;
    --map-tone-b: #e9ede4;
    --media-deep: #0f2a44;
    --media-mid: #2f6f9e;
    --media-light: #cfe6f5;
    --panel-white: #ffffff;
    --panel-frame: #9aa3ab;
    --brand: #111418;
  }
  * { margin: 0; padding: 0; box-sizing: border-box; }
  html, body {
    width: 1200px; height: 880px; overflow: hidden;
    background: var(--page-bg);
    font-family: "Montserrat", Arial, sans-serif;
    color: var(--ink);
  }
  .canvas {
    position: relative; width: 1200px; height: 880px;
    display: flex; align-items: center; justify-content: center; gap: 40px;
  }
  .card {
    position: relative; width: 540px; height: 309px;
    border-radius: 4px; overflow: hidden;
    box-shadow: 0 10px 28px rgba(0,0,0,0.18);
  }

  /* Front */
  .card--front {
    background: linear-gradient(160deg, var(--card-front) 0%, var(--card-front-edge) 100%);
  }
  .card__map {
    position: absolute; left: 315px; top: 150px; width: 225px; height: 159px;
    background: linear-gradient(135deg, var(--map-tone-a), var(--map-tone-b));
    opacity: 0.8;
  }
  .brand-lockup {
    display: flex; align-items: center; gap: 12px; white-space: nowrap;
  }
  .card--front .brand-lockup {
    position: absolute; left: 34px; top: 136px; width: 220px;
  }
  .brand-lockup__square {
    width: 30px; height: 30px; background: var(--brand); border-radius: 3px; flex: none;
  }
  .brand-lockup__name {
    font-weight: 800; font-size: 30px; letter-spacing: -0.5px; line-height: 1; color: var(--brand);
  }
  .card__divider {
    position: absolute; left: 270px; top: 42px; width: 1.5px; height: 225px;
    background: var(--divider);
  }
  .contact {
    position: absolute; left: 296px; top: 58px; width: 236px;
    font-size: 12.5px; line-height: 1.45; color: var(--ink-soft);
  }
  .contact__name { font-weight: 700; font-size: 15px; color: var(--ink); }
  .contact__role { font-style: italic; font-size: 11.5px; margin-bottom: 22px; }
  .contact__address { margin-bottom: 16px; }
  .contact__row { display: flex; align-items: center; gap: 12px; white-space: nowrap; }
  .contact__row svg { width: 11px; height: 11px; flex: none; fill: var(--ink); }
  .contact__group { margin-bottom: 16px; }

  /* Back */
  .card--back { background: var(--media-deep); }
  .card__media {
    position: absolute; inset: 0;
    background:
      radial-gradient(ellipse at 55% 45%, var(--media-light) 0%, rgba(207,230,245,0.4) 25%, transparent 60%),
      linear-gradient(135deg, var(--media-deep) 0%, var(--media-mid) 50%, var(--media-deep) 100%);
  }
  .back-panel {
    position: absolute; left: 155px; top: 92px; width: 230px; height: 125px;
    background: var(--panel-white);
    border: 5px solid var(--panel-frame);
    border-radius: 3px;
    display: flex; align-items: center; justify-content: center;
    box-shadow: 0 4px 12px rgba(0,0,0,0.35);
  }
  .back-panel .brand-lockup { gap: 10px; }
  .back-panel .brand-lockup__name { font-size: 28px; }
  .back-panel .brand-lockup__square { width: 26px; height: 26px; }
</style>
</head>
<body>
<main class="canvas">
  <section class="card card--front" aria-label="Business card front">
    <div class="card__map" role="img" aria-label="Faint street map backdrop"></div>
    <div class="brand-lockup">
      <span class="brand-lockup__square"></span>
      <span class="brand-lockup__name">Glowcast</span>
    </div>
    <div class="card__divider"></div>
    <div class="contact">
      <p class="contact__name">Name Surname</p>
      <p class="contact__role">function</p>
      <p class="contact__address">Your Address Goes Here<br>City, Country, Zipcode</p>
      <div class="contact__group">
        <p class="contact__row">
          <svg viewBox="0 0 12 12" aria-hidden="true"><path d="M2 1h3l1 3-1.5 1a6 6 0 0 0 2.5 2.5L8 6l3 1v3a1 1 0 0 1-1 1A9 9 0 0 1 1 2a1 1 0 0 1 1-1z"/></svg>
          (08) 5550 2741
        </p>
        <p class="contact__row">
          <svg viewBox="0 0 12 12" aria-hidden="true"><rect x="3" y="1" width="6" height="3"/><rect x="1" y="5" width="10" height="4" rx="1"/><rect x="3" y="8" width="6" height="3"/></svg>
          0400 555 318
        </p>
      </div>
      <p class="contact__row">
        <svg viewBox="0 0 12 12" aria-hidden="true"><path d="M1 3h10v7H1z M1 3l5 4 5-4" fill="var(--ink)" stroke="#fff" stroke-width="0.8"/></svg>
        name.surname@glowcast.com
      </p>
      <p class="contact__row">
        <svg viewBox="0 0 12 12" aria-hidden="true"><circle cx="6" cy="6" r="5" fill="none" stroke="var(--ink)" stroke-width="1.2"/><ellipse cx="6" cy="6" rx="2" ry="5" fill="none" stroke="var(--ink)" stroke-width="1"/><path d="M1 6h10" stroke="var(--ink)" stroke-width="1"/></svg>
        www.glowcast.com
      </p>
    </div>
  </section>

  <section class="card card--back" aria-label="Business card back">
    <div class="card__media" role="img" aria-label="Film strip of glowing media screens radiating from a bright centre"></div>
    <div class="back-panel">
      <div class="brand-lockup">
        <span class="brand-lockup__square"></span>
        <span class="brand-lockup__name">Glowcast</span>
      </div>
    </div>
  </section>
</main>
</body>
</html>
```